Professional Kiosk Poster for Logistics Trade Show

We need a graphic for our kiosk at a tradeshow. 38 13/16”W x 56 1/8”H.<br/><br/>We are a platform to match eCommerce parcel shipments with the most cost effective carrier for each package. We help eCommerce companies reduce their shipping costs and reduce the carbon impact of their shipments.<br/><br/>We would like to see something professional looking that incorporates our logo and the tag-line "Financially & Environmentally Sustainable eCommerce Shipping".<br/><br/>We would also like a call to action on the poster asking customers to contact "info@Velbrix.com"<br/><br/>Have included all logos we originally received. Can't open them on my own, as they're in formats I don't have software for. We use the blue and grey logo that can be seen on our website: www.velbrix.com<br/><br/>Design in line with our website would be appropriate. Have included potenaitl background images. Open to other options

Target Market(s)

Target is a business oriented trade show

Industry/Entity Type

Logistics

Colors

Designer to choose colors to be used in the design.

Requirements
Must have
• Must have company logo and contact information
Nice to have
• Nice to have our tagline. Nice to use a background image, although open to other options.
Should not have
• Should not be overly busy

```html
<!DOCTYPE html>
<html lang="en">
<head>
<meta charset="utf-8">
<title>Velbrix Kiosk Poster</title>
<link rel="stylesheet" href="https://fonts.googleapis.com/css2?family=Source+Sans+3:wght@400;600;700&display=swap">
<style>
  :root {
    --page-bg: #e9e9ea;
    --poster-dark: #0b0d12;
    --night-blue: #141a26;
    --street-amber: #6b4a2c;
    --street-glow: #a8773f;
    --road-dark: #2a2424;
    --brand-blue: #2aa7e1;
    --text-white: #ffffff;
  }
  * { margin: 0; padding: 0; box-sizing: border-box; }
  html, body {
    width: 1200px;
    height: 2400px;
    overflow: hidden;
    background: var(--page-bg);
    font-family: "Source Sans 3", "Myriad Pro", sans-serif;
  }
  .poster {
    position: absolute;
    left: 50px;
    top: 405px;
    width: 1100px;
    height: 1590px;
    overflow: hidden;
    background: var(--poster-dark);
    box-shadow: 0 10px 24px rgba(0,0,0,0.35);
  }
  .poster__photo {
    position: absolute;
    inset: 0;
    background:
      radial-gradient(ellipse 60% 18% at 50% 46%, rgba(168,119,63,0.55), transparent 70%),
      linear-gradient(180deg,
        var(--poster-dark) 0%,
        var(--night-blue) 22%,
        #2b2620 38%,
        var(--street-amber) 50%,
        var(--street-glow) 58%,
        var(--road-dark) 72%,
        #1a1516 84%,
        var(--poster-dark) 100%);
  }
  .poster__brand {
    position: absolute;
    top: 140px;
    left: 0;
    width: 100%;
    display: flex;
    justify-content: center;
    align-items: center;
    gap: 22px;
  }
  .brand__dot {
    width: 92px;
    height: 92px;
    border-radius: 50%;
    border: 12px solid var(--brand-blue);
  }
  .brand__name {
    font-weight: 700;
    font-size: 124px;
    line-height: 1;
    color: var(--brand-blue);
    letter-spacing: -2px;
  }
  .poster__tagline {
    position: absolute;
    top: 362px;
    left: 0;
    width: 100%;
    text-align: center;
    color: var(--text-white);
    font-weight: 700;
    font-size: 58px;
    line-height: 78px;
    text-shadow: 0 2px 8px rgba(0,0,0,0.5);
  }
  .poster__cta {
    position: absolute;
    top: 1314px;
    left: 0;
    width: 100%;
    text-align: center;
    color: var(--text-white);
    font-weight: 400;
    font-size: 29px;
    letter-spacing: 0.3px;
  }
  .poster__contact {
    position: absolute;
    top: 1384px;
    left: 125px;
    width: 861px;
    height: 84px;
    border-radius: 42px;
    background: var(--brand-blue);
    display: flex;
    justify-content: center;
    align-items: center;
    gap: 22px;
    color: var(--text-white);
    font-weight: 600;
    font-size: 35px;
  }
  .contact__divider {
    width: 3px;
    height: 38px;
    background: var(--text-white);
  }
</style>
</head>
<body>
  <main class="poster">
    <div class="poster__photo" role="img" aria-label="Night photograph of a busy city boulevard: lines of cars with headlights queued at a tunnel entrance beside an almost empty lane, under rows of ornate street lamps"></div>

    <header class="poster__brand">
      <span class="brand__dot"></span>
      <span class="brand__name">Velbrix</span>
    </header>

    <h1 class="poster__tagline">Financially &amp; Environmentally<br>Sustainable eCommerce Shipping</h1>

    <p class="poster__cta">FOR MORE INFORMATION PLEASE CONTACT US</p>

    <div class="poster__contact">
      <span class="contact__email">info@Velbrix.com</span>
      <span class="contact__divider"></span>
      <span class="contact__web">www.Velbrix.com</span>
    </div>
  </main>
</body>
</html>
```